Marketing Flyer for Plumber Referals

8.5" x11" Layout should be landscape not portrait. Create a bold, eye-catching flyer that highlights earning potential from referrals for water damage restoration. Use high-contrast colors like blue, yellow, and white, with bold fonts and dynamic layouts. Include images of restoration work, cash, and happy clients. Emphasize key benefits like $500 minimum payouts, fast payments, and unlimited income potential. Keep instructions simple: refer a client, we handle the work, you get paid. Add a clear call-to-action and display contact details prominently. Focus on professionalism and energy.

Target Market(s)

Plumbers and Contractor 8.5" x11" Layout should be landscape not portrait.

Industry/Entity Type

General Contractor

Colors
0054AA
0677BA
7BADD7
CADEEF
E8F1F8
EB3D1F
EC4F4E
F09395
F8D3D4
FCEDEE

Requirements
Must have
• 8.5" x11" Layout should be landscape not portrait.
Nice to have

```html
<!DOCTYPE html>
<html lang="en">
<head>
<meta charset="utf-8">
<title>Refer a Flood – Plumber Referral Flyer</title>
<link rel="stylesheet" href="https://fonts.googleapis.com/css2?family=Bebas+Neue&family=Roboto:wght@400;500;700&family=Roboto+Condensed:wght@700&display=swap">
<style>
  :root {
    --blue-deep: #0677BA;
    --blue-bright: #2AA9E0;
    --ink: #111111;
    --yellow: #F9EC24;
    --white: #ffffff;
    --photo-cash-a: #d9ddd2;
    --photo-cash-b: #8fa89a;
    --photo-flood-a: #e9e7e2;
    --photo-flood-b: #9a9690;
    --photo-pipe-a: #f2f2f2;
    --photo-pipe-b: #6f6f72;
  }
  * { margin: 0; padding: 0; box-sizing: border-box; }
  html, body { width: 1200px; height: 674px; overflow: hidden; background: var(--white); }
  .flyer {
    position: relative;
    width: 1200px;
    height: 674px;
    overflow: hidden;
    background: var(--white);
    font-family: 'Roboto', Arial, sans-serif;
    color: var(--ink);
  }
  .headline { position: absolute; left: 0; top: 0; overflow: visible; }
  .headline text { font-family: 'Bebas Neue', Impact, sans-serif; }
  .headline .shadow { fill: var(--blue-bright); }
  .headline .face { fill: var(--blue-deep); }

  .partner {
    position: absolute;
    left: 48px;
    top: 272px;
    font-weight: 500;
    font-size: 33px;
    line-height: 41px;
  }
  .partner .team { color: var(--blue-bright); }

  .benefits {
    position: absolute;
    left: 53px;
    top: 377px;
  }
  .benefits h2 {
    font-family: 'Roboto Condensed', 'Arial Narrow', sans-serif;
    font-weight: 700;
    font-size: 18px;
    color: var(--blue-bright);
    margin-bottom: 12px;
  }
  .benefit-list { list-style: none; }
  .benefit-list li {
    display: flex;
    font-size: 17px;
    height: 32px;
    line-height: 22px;
  }
  .benefit-list .label {
    font-family: 'Roboto Condensed', 'Arial Narrow', sans-serif;
    font-weight: 700;
    width: 173px;
  }
  .benefit-list .detail::before { content: ": "; font-weight: 700; }

  .photo {
    position: absolute;
    border-radius: 50%;
  }
  .photo-cash {
    left: 732px; top: 243px; width: 186px; height: 186px;
    background: radial-gradient(circle at 45% 40%, var(--photo-cash-a), var(--photo-cash-b));
  }
  .photo-flood {
    left: 885px; top: 183px; width: 270px; height: 270px;
    background: linear-gradient(180deg, var(--photo-flood-a) 0%, #cfc7b8 45%, var(--photo-flood-b) 100%);
  }
  .photo-pipe {
    left: 824px; top: 335px; width: 254px; height: 254px;
    border: 5px solid var(--white);
    background: radial-gradient(circle at 55% 40%, var(--photo-pipe-a), var(--photo-pipe-b));
  }

  .wave { position: absolute; left: 0; top: 530px; }
  .wave .band { fill: var(--yellow); }
  .wave .edge { fill: none; stroke: var(--blue-deep); stroke-width: 7; }

  .cta {
    position: absolute;
    left: 48px;
    top: 595px;
    font-size: 29px;
    line-height: 34px;
  }
  .cta strong { display: block; font-weight: 700; font-size: 28px; }
</style>
</head>
<body>
<main class="flyer">
  <svg class="headline" width="1200" height="250" viewBox="0 0 1200 250" aria-label="Earn unlimited cash. Get paid to refer a flood">
    <text class="shadow" x="48" y="155" font-size="150" textLength="960" lengthAdjust="spacingAndGlyphs">EARN UNLIMITED CASH</text>
    <text class="face" x="45" y="152" font-size="150" textLength="960" lengthAdjust="spacingAndGlyphs">EARN UNLIMITED CASH</text>
    <text class="shadow" x="46" y="236" font-size="90" textLength="717" lengthAdjust="spacingAndGlyphs">GET PAID TO REFER A FLOOD</text>
    <text class="face" x="44" y="234" font-size="90" textLength="717" lengthAdjust="spacingAndGlyphs">GET PAID TO REFER A FLOOD</text>
  </svg>

  <p class="partner">Partner with<br>the #1 <span class="team">Water Damage Restoration Team</span></p>

  <section class="benefits">
    <h2>Why Partner with Us?</h2>
    <ul class="benefit-list">
      <li><span class="label">Guaranteed Payout</span><span class="detail">Minimum $500 or 10% of the invoice, paid fast.</span></li>
      <li><span class="label">Free Evaluations</span><span class="detail">We assess damage and process insurance claims for your clients.</span></li>
      <li><span class="label">Industry Leaders</span><span class="detail">Certified experts with 24/7 rapid response.</span></li>
      <li><span class="label">Affordable Solutions</span><span class="detail">Lowest out-of-pocket costs for your customers.</span></li>
    </ul>
  </section>

  <div class="photo photo-flood" role="img" aria-label="Flooded room with water covering the floor at the foot of a staircase"></div>
  <div class="photo photo-cash" role="img" aria-label="Banknotes with letter tiles spelling cash flow"></div>
  <div class="photo photo-pipe" role="img" aria-label="White drain pipe leaking water"></div>

  <svg class="wave" width="1200" height="144" viewBox="0 0 1200 144" aria-hidden="true">
    <path class="band" d="M0 48 C 220 18, 420 28, 720 104 C 900 140, 1050 80, 1200 10 L1200 144 L0 144 Z"/>
    <path class="edge" d="M0 48 C 220 18, 420 28, 720 104 C 900 140, 1050 80, 1200 10"/>
  </svg>

  <p class="cta"><strong>SEND REFERRALS.</strong>GET PAID. GROW YOUR BUSINESS</p>
</main>
</body>
</html>
```